Wren's Hearth Support Business Card

Business card design
Font must be in Poppins Regular for Wren's Hearth Support
Safe Days Ahead font is Alex Brush

Colour must be Hex #910E2B
RGB 145-14-43
Pantone 7427 C
We want the card editable
On the front please include
Name eg Mavis Dunleavy
Position eg Clinical Care Manager
Phone number mobile 0473 856 342
Phone 08 7394 2650
Email : mavis@wrenshearthsupport.com.au
Address : Gullwing Cove, Tallow Region, 6291
Website : wrenshearthsupport.com.au
Contact us today to experience the warmth, respect and personal touch of Wren's Hearth Support.

Target Market(s)

35+

Industry/Entity Type

aged care / community

Contact Information for Business Card

see project description

Requirements
Must have
• Colours, logos and fonts as detailed and uploaded

```html
<!DOCTYPE html>
<html lang="en">
<head>
<meta charset="utf-8">
<title>Wren's Hearth Support – Business Card</title>
<link rel="stylesheet" href="https://fonts.googleapis.com/css2?family=Alex+Brush&family=Poppins:wght@400&display=swap">
<style>
  :root {
    --page-bg: #d9d9d9;
    --card-deep: #650720;
    --brand-red: #910e2b;
    --sand: #e0b68c;
    --white: #ffffff;
  }
  * { margin: 0; padding: 0; box-sizing: border-box; }
  html, body {
    width: 1200px;
    height: 2871px;
    overflow: hidden;
    background: var(--page-bg);
    font-family: "Poppins", sans-serif;
    font-weight: 400;
  }
  .canvas { position: relative; width: 1200px; height: 2871px; }

  .card {
    position: absolute;
    left: 309px;
    width: 606px;
    height: 350px;
    background: var(--card-deep);
  }
  .card--front { top: 282px; }
  .card--back { top: 677px; }

  .front__strap {
    position: absolute;
    top: 10px; left: 0; right: 0;
    text-align: center;
    font-size: 9.5px;
    color: var(--sand);
    white-space: nowrap;
  }
  .front__panel {
    position: absolute;
    left: 14px; top: 28px;
    width: 156px; height: 287px;
    background: var(--brand-red);
  }
  .front__name {
    position: absolute;
    left: 197px; top: 80px;
    font-size: 42px;
    font-weight: 400;
    line-height: 1;
    color: var(--white);
    white-space: nowrap;
  }
  .front__role {
    position: absolute;
    left: 200px; top: 120px;
    font-family: "Alex Brush", cursive;
    font-size: 22px;
    color: var(--sand);
    white-space: nowrap;
  }
  .front__contacts {
    position: absolute;
    left: 198px; top: 196px;
    list-style: none;
    font-size: 16.5px;
    line-height: 22.5px;
    color: var(--white);
  }
  .front__contacts .address { margin-top: 3px; line-height: 20.5px; }

  .back__field {
    position: absolute;
    left: 14px; top: 28px;
    width: 575px; height: 287px;
    background: var(--brand-red);
  }
  .brand {
    position: absolute;
    left: 160px; top: 96px;
    display: flex;
    align-items: center;
    gap: 8px;
  }
  .brand__dot {
    width: 80px; height: 80px;
    border-radius: 50%;
    background: var(--sand);
    flex: none;
  }
  .brand__name {
    font-size: 29px;
    line-height: 30px;
    color: var(--sand);
  }
  .brand__tagline {
    font-family: "Alex Brush", cursive;
    font-size: 19px;
    line-height: 1;
    color: var(--sand);
    margin-top: 4px;
  }
  .back__web {
    position: absolute;
    left: 0; right: 0; top: 258px;
    text-align: center;
    font-size: 14.5px;
    line-height: 20px;
    letter-spacing: 3px;
    color: var(--white);
  }
</style>
</head>
<body>
<main class="canvas">

  <section class="card card--front" aria-label="Business card front">
    <p class="front__strap">Contact us today to experience the warmth, respect and personal touch of Wren's Hearth Support.</p>
    <div class="front__panel" role="img" aria-label="Brand red panel with large sand-coloured flower emblem"></div>
    <h1 class="front__name">Mavis Dunleavy</h1>
    <p class="front__role">Clinical Care Manager</p>
    <ul class="front__contacts">
      <li>0473 856 342</li>
      <li>08 7394 2650</li>
      <li>mavis@wrenshearthsupport.com.au</li>
      <li class="address">Gullwing Cove, Tallow<br>Region, 6291</li>
    </ul>
  </section>

  <section class="card card--back" aria-label="Business card back">
    <div class="back__field">
      <div class="brand">
        <span class="brand__dot"></span>
        <div>
          <p class="brand__name">Wren's<br>Hearth Support</p>
          <p class="brand__tagline">Safe Days Ahead</p>
        </div>
      </div>
      <p class="back__web">www.wrenshearthsupport.com.au</p>
    </div>
  </section>

</main>
</body>
</html>
```